Are You Ready For The Next Hail Storm?

We need a two paged (Front and Back) flyer to educate our potential clients to what our company does.
I have included some previous pamphlets along with products we carry.
Want a info-tutorial on what we do for the clients and how they can sign up.
One page both sides type of pamphlet.
Clear steps as to how we can help them and to have the peace of mind knowing their home is protected.
Our mantra is : Happy Homes, Protected By Experts, Built By Trust.

Target Market(s)

Home Owners worried about storm events.

Industry/Entity Type

Insurance

Requirements
Must have
• (Logo Package Uploaded - 1960's feel to our company)
Home Protection Package:
Sign up today @ StormGuardPlan.com
Discount Code - ROOFSAFE
We take all the worry from homeowners. Our Homeowner Hail/Wind Protection Package includes 24/7/365 monitoring of property for hail events. Emergency crews to close up any windows or roof leaks. Educational Information and Review of Current Policy.
Emergency Response: 1 - Damage triage. 2 - Mitigate Further Damage. 3 - Inspect and Assess. 4 - Deal with Insurance on Your Behalf To Maximize Your Home Claim. 5 - Restoration of Home With The Proper Funding From Your Insurance Claim.
Insurance Liaison Option.
Sign up @ www.FairPayoutDesk.com
www.TheRebuildMedic.com
Our Commitment:
30 minute first contact.
Onsite within hours.
Thorough documentation.
Empathy and care handling your complete claim.
Full warranty package registered on your behalf.
24/7/365 Service

PSL Registered
2 Million General Liability
Calgary Business License
Civic Vendor Council A+ Accreditation
Nice to have
• Walk the home owners through a visual and text pamphlet.

```html
<!DOCTYPE html>
<html lang="en">
<head>
<meta charset="utf-8">
<title>Home Protection Flyer</title>
<link rel="stylesheet" href="https://fonts.googleapis.com/css2?family=Bebas+Neue&family=Montserrat:wght@400;500;600;700;800&display=swap">
<style>
:root{
  --navy:#2c3856;
  --navy-dark:#232d47;
  --gold:#f7b731;
  --gold-light:#fdd56b;
  --white:#ffffff;
  --stage:#5d5d5d;
  --head:'Bebas Neue',sans-serif;
  --body:'Montserrat',sans-serif;
}
*{margin:0;padding:0;box-sizing:border-box}
html,body{width:1200px;height:1200px;overflow:hidden}
body{background:var(--stage);font-family:var(--body);position:relative}
.page{position:absolute;top:204px;width:570px;height:792px;overflow:hidden;background:var(--navy);color:var(--white)}
.page--front{left:20px}
.page--back{left:610px}
.abs{position:absolute}
.txt{font-size:7.6px;line-height:1.45;color:var(--white)}
.section-title{font-family:var(--body);font-weight:700;font-size:12px;color:var(--gold)}

/* front */
.front__top{left:0;top:0;width:570px;height:161px;background:var(--white)}
.brand{display:flex;align-items:center;gap:7px;font-family:var(--body);font-weight:800;color:var(--navy);white-space:nowrap}
.brand__dot{border-radius:50%;background:var(--gold);flex:none}
.front__brand{left:45px;top:68px;font-size:19px}
.front__brand .brand__dot{width:20px;height:20px}
.shield{left:280px;top:4px}
.hero__title{left:35px;top:178px;font-family:var(--head);font-size:54px;line-height:1;color:var(--gold);white-space:nowrap}
.hero__sub{left:35px;top:228px;font-family:var(--head);font-size:30px;line-height:1;color:var(--white);white-space:nowrap}
.hero__tag{left:36px;top:287px;width:226px;height:22px;background:var(--gold);border:1px solid var(--white);font-family:var(--head);font-size:11px;letter-spacing:.1px;color:var(--navy);display:flex;align-items:center;justify-content:center;white-space:nowrap}
.welcome{left:333px;top:428px;width:220px}
.welcome__label{font-weight:700;font-size:17px;color:var(--gold);display:inline-block;border-bottom:1.5px solid var(--gold);padding-bottom:1px}
.welcome__title{margin-top:8px;font-weight:700;font-size:16.5px;line-height:1.07;color:var(--white)}
.welcome__option{margin-top:3px;font-weight:700;font-size:11px;color:var(--gold)}
.btn{display:inline-block;margin-top:8px;background:var(--white);color:var(--navy);font-weight:700;font-size:11.5px;padding:5px 11px;border-radius:14px}
.welcome__links{margin-top:10px;font-size:9.5px;font-weight:600;color:var(--gold);line-height:1.7}
.badge24{left:100px;top:560px}
.front__band{left:0;top:666px;width:570px;height:79px;background:linear-gradient(90deg,var(--gold-light),var(--gold))}
.hire{font-weight:700;color:var(--navy);white-space:nowrap}
.hire__lead{font-size:8.6px}
.hire__phone{display:flex;align-items:center;gap:7px;font-weight:800;line-height:1}
.hire__plan{font-weight:700}
.front__hire{left:35px;top:674px}
.front__hire .hire__phone{font-size:28px;margin-top:3px}
.front__hire .hire__plan{font-size:15.5px;margin-top:3px}
.package{left:358px;top:599px;width:122px;height:122px;border-radius:50%;background:var(--gold);border:3px solid var(--navy);overflow:hidden;text-align:center}
.package__name{margin-top:12px;font-weight:700;font-size:11.5px;line-height:1.07;color:var(--navy)}
.package__code{position:absolute;left:0;right:0;top:62px;bottom:0;background:var(--white);padding-top:4px;font-size:10px;font-weight:500;color:var(--navy)}
.package__chip{display:inline-block;margin-top:3px;border:1px dashed var(--navy);border-radius:9px;padding:1px 9px;font-weight:700;font-size:10px}
.package__signup{left:350px;top:707px;width:138px;height:31px;background:var(--navy);border-radius:4px;text-align:center;font-size:10px;font-weight:600;color:var(--gold);line-height:1.2;padding-top:3px}
.front__contact{top:761px;font-size:9.5px;font-weight:500;color:var(--gold);display:flex;align-items:center;gap:4px}
.mini-dot{width:9px;height:9px;border-radius:50%;background:var(--gold)}

/* back */
.photo{height:58px;width:140px;border:2px solid var(--gold)}
.service__title{font-weight:700;font-size:9.5px;line-height:1.35;color:var(--gold)}
.divider{width:0;border-left:1px dashed var(--gold);top:105px;height:185px}
.tree{left:0;top:312px}
.step__box{top:354px;width:82px;height:27px;border-radius:3px;background:linear-gradient(180deg,var(--gold-light),var(--gold));border:1px solid var(--white);font-size:6.3px;font-weight:700;color:var(--navy);text-align:center;line-height:1.15;display:flex;align-items:center;justify-content:center}
.step__text{top:390px;width:92px;font-size:7.6px;line-height:1.22}
.commit{left:0;top:540px;width:570px;height:157px;background:linear-gradient(90deg,var(--gold-light),var(--gold))}
.commit__title{left:33px;top:553px;font-weight:800;font-size:15px;color:var(--navy);border-bottom:1.5px solid var(--navy);padding-bottom:4px;padding-right:35px}
.commit__list{list-style:none;font-size:8px;font-weight:500;color:var(--navy);white-space:nowrap}
.commit__list li{height:18.2px;display:flex;align-items:flex-start;gap:6px}
.commit__list li::before{content:"";width:4px;height:4px;border-radius:50%;background:var(--navy);margin-top:3px;flex:none}
.mascot{left:452px;top:512px;width:108px;height:182px;border-radius:50% 50% 12px 12px;background:radial-gradient(circle at 50% 35%,#eef2f5,#9ec1c7 55%,rgba(44,56,86,.55))}
.back__footer{left:0;top:700px;width:570px;height:92px;background:var(--white)}
.back__strip{left:0;top:697px;width:570px;height:3px;background:var(--navy)}
.back__brand{left:30px;top:741px;font-size:9px;font-weight:700;gap:5px}
.back__brand .brand__dot{width:10px;height:10px}
.back__hire{left:158px;top:722px}
.back__hire .hire__lead{font-size:8px}
.back__hire .hire__phone{font-size:24px;margin-top:3px}
.back__hire .hire__plan{font-size:13.5px;margin-top:2px}
.back__contact{left:390px;font-size:7.6px;font-weight:500;color:var(--navy);display:flex;align-items:center;gap:4px;white-space:nowrap}
.back__contact .mini-dot{background:var(--navy);width:8px;height:8px}
</style>
</head>
<body>

<section class="page page--front">
  <div class="abs front__top"></div>
  <div class="abs brand front__brand"><span class="brand__dot"></span>The Rebuild Medic</div>

  <svg class="abs shield" width="290" height="420" viewBox="0 0 290 420">
    <defs>
      <linearGradient id="storm" x1="0" y1="0" x2="0" y2="1">
        <stop offset="0" stop-color="#3d4a4f"/>
        <stop offset=".4" stop-color="#7d8a86"/>
        <stop offset=".6" stop-color="#c9b8ad"/>
        <stop offset="1" stop-color="#4f7a2f"/>
      </linearGradient>
    </defs>
    <rect x="76" y="24" width="20" height="40" fill="var(--navy)"/>
    <path d="M184,8 L360,100 L360,260 Q320,350 184,418 Q60,340 4,210 L4,92 Z" fill="var(--gold)"/>
    <path d="M188,0 L360,90 L360,250 Q320,340 188,408 Q68,330 12,200 L12,84 Z" fill="var(--navy)"/>
    <path d="M188,38 L360,118 L360,240 Q320,316 188,380 Q86,312 42,196 L42,112 Z" fill="url(#storm)" stroke="var(--white)" stroke-width="5" role="img" aria-label="Photo of a suburban house under dark storm clouds with green lawn"/>
  </svg>

  <div class="abs hero__title">HAPPY HOMES</div>
  <div class="abs hero__sub">PROTECTED BY EXPERTS<br>BUILT BY TRUST</div>
  <div class="abs hero__tag">HAVE YOU BEEN DISAPPOINTED BY YOUR INSURANCE COMPANY?</div>

  <p class="abs txt" style="left:35px;top:318px;width:285px">We work for YOU.... Not the insurance companies! Let our trained professionals take the worry off your shoulders.</p>

  <h3 class="abs section-title" style="left:35px;top:340px">ABOUT US</h3>
  <p class="abs txt" style="left:35px;top:354px;width:345px">We work for the homeowner. Simple as that! If there is a disaster that hits and you need help call us, 24/7. The insurance process can be daunting especially with the added stress of your biggest investment being vulnerable. hail restoration contractor hail siding roofing building restoration</p>

  <h3 class="abs section-title" style="left:35px;top:409px">WORKING TOGETHER</h3>
  <p class="abs txt" style="left:35px;top:424px;width:273px;text-align:justify;line-height:1.6">We offer an end-to-end client experience that includes seamless communication, representing you with the insurance company, getting the most value and justifying the extended claim, project management from start to finish in the restoration project.</p>

  <h3 class="abs section-title" style="left:35px;top:477px">WHY CHOOSE US?</h3>
  <p class="abs txt" style="left:35px;top:492px;width:273px;text-align:justify;line-height:1.6">We work for you, communicating with your best interest in mind. Don't let the insurance company take advantage of you. Call us today and bring our project management skills and extensive construction experience into your disaster and we will make it BETTER THAN before!</p>

  <svg class="abs badge24" width="120" height="104" viewBox="0 0 120 104">
    <circle cx="62" cy="52" r="48" fill="none" stroke="var(--gold)" stroke-width="1.5" stroke-dasharray="1.5 4"/>
    <text x="6" y="54" font-family="Montserrat, sans-serif" font-weight="800" font-size="32" fill="var(--white)">24</text>
    <text x="52" y="36" font-family="Montserrat, sans-serif" font-weight="700" font-size="12" fill="var(--gold)">OPEN</text>
    <text x="50" y="55" font-family="Montserrat, sans-serif" font-weight="800" font-size="16" fill="var(--white)">hrs</text>
    <text x="30" y="76" font-family="Montserrat, sans-serif" font-weight="800" font-size="16" fill="var(--gold)">Services</text>
  </svg>

  <div class="abs welcome">
    <div class="welcome__label">WELCOME</div>
    <div class="welcome__title">THE PROPER<br>FUNDING FROM YOUR<br>INSURANCE CLAIM</div>
    <div class="welcome__option">INSURANCE LIAISON OPTION</div>
    <div class="btn">SIGN UP NOW</div>
    <div class="welcome__links">@ www.FairPayoutDesk.com<br>www.TheRebuildMedic.com</div>
  </div>

  <div class="abs front__band"></div>
  <div class="abs hire front__hire">
    <div class="hire__lead">FOR THE COMPLETE CARE OF HOME HIRE US!</div>
    <div class="hire__phone">
      <svg width="24" height="24" viewBox="0 0 24 24"><circle cx="12" cy="12" r="12" fill="var(--navy)"/><path d="M8 5.5l2.3 2.6-1.2 2a8 8 0 004.8 4.8l2-1.2 2.6 2.3-1.3 2.4c-5 .3-10.9-5.6-10.6-10.6z" fill="var(--gold)"/></svg>
      403 555 0187
    </div>
    <div class="hire__plan">AFFORDABLE SERVIE PLAN</div>
  </div>

  <div class="abs package">
    <div class="package__name">HOME<br>PROTECTION<br>PACKAGE</div>
    <div class="package__code">Discount Code<br><span class="package__chip">ROOFSAFE</span></div>
  </div>
  <div class="abs package__signup">Sign up today<br>@ StormGuardPlan.com</div>

  <div class="abs front__contact" style="left:78px"><span class="mini-dot"></span>claims@therebuildmedic.com</div>
  <div class="abs front__contact" style="left:312px"><span class="mini-dot"></span>www.therebuildmedic.com</div>
</section>

<section class="page page--back">
  <h3 class="abs section-title" style="left:33px;top:42px">SERVICES</h3>
  <p class="abs txt" style="left:33px;top:57px;width:505px;text-align:justify;line-height:1.4">We take all the worry from homeowners. Our Homeowner Hail/Wind Protection Package includes 24/7/365 monitoring of property for hail events. Emergency crews to close up any windows or roof leaks. Educational Information and Review of Current Policy.</p>

  <div class="abs photo" style="left:34px;top:105px;background:linear-gradient(180deg,#b9c7d3,#6e8a5a 45%,#9a7a4e)" role="img" aria-label="Aerial photo of a flooded neighbourhood"></div>
  <div class="abs photo" style="left:210px;top:105px;background:linear-gradient(90deg,#1e2a3c,#3d79b8 55%,#a9cbe8)" role="img" aria-label="Photo of a hand touching home insurance icons"></div>
  <div class="abs photo" style="left:393px;top:105px;background:linear-gradient(90deg,#c9c9c9,#eeeeee 50%,#a9774b)" role="img" aria-label="Photo of a worker in protective suit sanitizing a room"></div>

  <div class="abs divider" style="left:195px"></div>
  <div class="abs divider" style="left:372px"></div>

  <h4 class="abs service__title" style="left:34px;top:172px">HAIL RESTORATION FIRE &amp;<br>FLOOD RESTORATION</h4>
  <p class="abs txt" style="left:34px;top:199px;width:140px;line-height:1.32">When homeowners are hit by disaster we can deploy a team of experts to preform triage and get your home patched up till we can restore back to better!</p>
  <h4 class="abs service__title" style="left:215px;top:172px">INSURANCE LIAISON</h4>
  <p class="abs txt" style="left:215px;top:199px;width:140px;line-height:1.32">Working with trusted subcontractors, we keep them accountable throughout the entire build. From sequence to production and quality control, we stay focused on the goal.</p>
  <h4 class="abs service__title" style="left:396px;top:172px">COVID 19 PREVENTION &amp;<br>SANITIZATION</h4>
  <p class="abs txt" style="left:396px;top:199px;width:140px;line-height:1.32">The last step in any build. This phase includes site cleanup, systems training, final inspections and move-in coordination. After completion, we have a final walkthrough to ensure your complete satisfaction.</p>

  <h3 class="abs section-title" style="left:33px;top:300px">EMERGENCY RESPONSE</h3>
  <svg class="abs tree" width="570" height="45" viewBox="0 0 570 45">
    <g stroke="#cfd4de" stroke-width="1" fill="none">
      <path d="M105 5V22M75 22H481M75 22V40M177 22V40M279 22V40M381 22V40M481 22V40"/>
    </g>
    <g fill="var(--gold)">
      <circle cx="75" cy="40" r="2.2"/><circle cx="177" cy="40" r="2.2"/><circle cx="279" cy="40" r="2.2"/><circle cx="381" cy="40" r="2.2"/><circle cx="481" cy="40" r="2.2"/>
    </g>
  </svg>

  <div class="abs step__box" style="left:34px">DAMAGE<br>TRIAGE</div>
  <div class="abs step__box" style="left:136px">MITIGATE FURTHER<br>DAMAGE</div>
  <div class="abs step__box" style="left:238px">INSPECT AND<br>ASSESS</div>
  <div class="abs step__box" style="left:340px">DEAL WITH<br>INSURANCE</div>
  <div class="abs step__box" style="left:442px">RESTORATION<br>OF HOME</div>

  <p class="abs txt step__text" style="left:33px">When a fire occurs it caused extreme distress on our clients and greatly impacts lives and business a like. Our expert team of technicians are highly trained in addressing all damages of a fire and fully restoring the structure.</p>
  <p class="abs txt step__text" style="left:136px">A condition in almost every insurance policy is that the insured must mitigate the loss to prevent further damages. Meaning it is your responsibility as the insured to take reasonable action to avoid secondary damages, or at least to reduce them.</p>
  <p class="abs txt step__text" style="left:238px">We discuss building safety &amp; damage assessment following earthquake, fire, flood, hurricane, windstorm or similar catastrophes. The articles in this series explain safe building entry procedures, priority of action or repair, and also damage prevention.</p>
  <p class="abs txt step__text" style="left:340px">Once you sign up with our Home Insurance Liaison Terms of Service we deploy our inspection team, evaluate your house damages, and do a complete presentation package for your insurance provider.</p>
  <p class="abs txt step__text" style="left:442px">When you received your claim amount were you disappointed or confused? Feeling helpless? LET US HELP!! We have increased our clients claims by tens of thousands of dollars! Every single client we have helped increase claim value.</p>

  <div class="abs commit"></div>
  <div class="abs mascot" role="img" aria-label="Illustrated cartoon doctor mascot with clipboard and stethoscope"></div>
  <h3 class="abs commit__title">OUR COMMITMENT:</h3>
  <ul class="abs commit__list" style="left:33px;top:588px">
    <li>30 minute first contact.</li>
    <li>Onsite within hours.</li>
    <li>Thorough documentation.</li>
    <li>Empathy and care handling your complete claim.</li>
    <li>Full warranty package registered on your behalf.</li>
    <li>24/7/365 Service</li>
  </ul>
  <ul class="abs commit__list" style="left:266px;top:588px">
    <li>PSL Registered</li>
    <li>2 Million General Liability</li>
    <li>Calgary Business License</li>
    <li>Civic Vendor Council A+ Accreditation</li>
  </ul>

  <div class="abs back__strip"></div>
  <div class="abs back__footer"></div>
  <div class="abs brand back__brand"><span class="brand__dot"></span>The Rebuild Medic</div>
  <div class="abs hire back__hire">
    <div class="hire__lead">FOR THE COMPLETE CARE OF HOME HIRE US!</div>
    <div class="hire__phone">
      <svg width="21" height="21" viewBox="0 0 24 24"><circle cx="12" cy="12" r="12" fill="var(--navy)"/><path d="M8 5.5l2.3 2.6-1.2 2a8 8 0 004.8 4.8l2-1.2 2.6 2.3-1.3 2.4c-5 .3-10.9-5.6-10.6-10.6z" fill="var(--white)"/></svg>
      403 555 0187
    </div>
    <div class="hire__plan">AFFORDABLE SERVIE PLAN</div>
  </div>
  <div class="abs back__contact" style="top:750px"><span class="mini-dot"></span>claims@therebuildmedic.com</div>
  <div class="abs back__contact" style="top:767px"><span class="mini-dot"></span>www.therebuildmedic.com</div>
</section>

</body>
</html>
```